Lumora Assist overview brochure

Take the word document that is attached and turn it into a brochure. (Thinking one page, front and back.) the only existing branding/colors we have is the logo that is on the document. It may require a phone all or a bit of back and forth in text to explain some of the concepts in the attached document.

Target Market(s)

Call centers

Industry/Entity Type

It Service

Font styles to use
Sans Serif

Colors

Designer to choose colors to be used in the design.

Requirements
Must have
• A crisp professional look

```html
<!DOCTYPE html>
<html lang="en">
<head>
<meta charset="utf-8">
<title>Lumora Assist overview brochure</title>
<link href="https://fonts.googleapis.com/css2?family=Cinzel:wght@400;600&family=Roboto:wght@400;500&display=swap" rel="stylesheet">
<style>
:root{
  --blue:#29a3dc;
  --blue-dark:#1d86bb;
  --ink:#2f3033;
  --charcoal:#3b3c3f;
  --paper:#ffffff;
  --mist:#eef2f5;
  --stage:#e6e7e9;
  --white:#ffffff;
}
*{margin:0;padding:0;box-sizing:border-box}
html,body{width:1200px;height:1200px;overflow:hidden}
body{background:var(--stage);font-family:"Roboto",Arial,sans-serif;position:relative}
.sheet{position:absolute;top:220px;width:540px;height:760px;background:var(--paper);box-shadow:0 4px 14px rgba(0,0,0,.18);overflow:hidden}
.sheet--front{left:40px}
.sheet--back{left:620px}
.abs{position:absolute}
.brand{display:flex;align-items:center;gap:8px}
.brand__dot{width:26px;height:26px;border-radius:50%;background:var(--blue)}
.brand__name{font-family:"Cinzel",Georgia,serif;font-weight:600;color:var(--blue);font-size:18px;line-height:1}
/* front */
.front-header{top:0;left:0;width:540px;height:74px;display:flex;justify-content:center;align-items:center;border-bottom:4px solid var(--charcoal)}
.hero-photo{top:78px;left:0;width:540px;height:242px;background:linear-gradient(180deg,#4f6e8e 0%,#9fa9b0 40%,#e2c48f 56%,#6b5a48 66%,#1b1d22 100%)}
.hero-accent{top:316px;left:0;width:300px;height:6px;background:var(--blue)}
.headline{top:336px;left:30px;width:480px;text-align:center;font-family:"Cinzel",Georgia,serif;font-size:15.5px;line-height:1.15;color:var(--ink);letter-spacing:.3px}
.intro{top:414px;left:0;width:272px;height:309px;background:var(--blue);padding:16px 14px 10px 0}
.intro__body{border-left:1.5px solid var(--white);margin-left:20px;padding-left:11px;color:var(--white);font-size:8.3px;line-height:1.3;text-align:justify}
.intro__body p+p{margin-top:10px}
.channels{top:414px;left:272px;width:268px;height:309px;background:var(--mist);padding:14px 14px 0 16px}
.channels__title{font-family:"Cinzel",Georgia,serif;font-size:10px;color:var(--ink);letter-spacing:.3px}
.channels__title span{color:var(--blue);text-decoration:underline}
.channel-row{display:flex;align-items:center;gap:10px;margin-top:9px}
.channel-row__icon{width:22px;height:22px;flex:none}
.channel-row__text{font-family:"Cinzel",Georgia,serif;font-size:9.4px;line-height:1.2;color:var(--ink)}
.channel-row__text em{color:var(--blue);font-family:Georgia,serif;font-style:italic}
.footnote{margin:10px 0 0 4px;width:222px;background:var(--charcoal);color:var(--white);font-size:7.8px;text-align:center;border-radius:8px;padding:2px 0}
.cloud-photo{margin-top:8px;width:240px;height:122px;background:linear-gradient(135deg,#7f8d96 0%,#3c4a58 55%,#1f2b3a 100%);box-shadow:0 2px 5px rgba(0,0,0,.3)}
.front-footer{top:723px;left:0;width:540px;height:37px;background:var(--charcoal);color:var(--white);font-size:10px;font-weight:500}
.front-footer__slash{top:0;left:270px;width:18px;height:37px;background:var(--white);transform:skewX(-14deg)}
.contact{display:flex;align-items:center;gap:8px}
/* back */
.back-top{top:0;left:0;width:540px;height:122px}
.app-strip{top:22px;left:28px;width:484px;height:62px;border:1.5px solid #9aa1a7;border-radius:12px;box-shadow:4px 4px 0 var(--blue);display:flex;justify-content:space-around;align-items:center;padding:0 8px;background:var(--white)}
.app{display:flex;flex-direction:column;align-items:center;gap:3px;font-size:7.5px;color:var(--ink);font-weight:500}
.app__mark{width:26px;height:26px;border-radius:6px;background:var(--blue)}
.strip-note{top:98px;left:0;width:540px;text-align:center;font-size:7.9px;color:var(--ink);font-weight:500}
.engagement{top:122px;left:0;width:324px;height:570px;background:var(--blue);color:var(--white);padding:14px 12px 0 30px;font-size:10px;line-height:1.25}
.section-title{font-family:"Cinzel",Georgia,serif;font-weight:600;color:var(--ink);font-size:13px;letter-spacing:.3px}
.section-title u{text-decoration-thickness:1px}
.sub-title{font-family:"Cinzel",Georgia,serif;font-weight:600;color:var(--ink);font-size:10.5px;margin-top:8px}
.ticks{list-style:none;margin-top:6px}
.ticks li{position:relative;padding-left:13px;margin-bottom:5px}
.ticks li::before{content:"";position:absolute;left:0;top:3px;width:6px;height:6px;border:1.2px solid rgba(255,255,255,.85);border-radius:50%}
.portrait-panel{top:122px;left:324px;width:216px;height:570px;background:radial-gradient(circle at 50% 25%,#8d8d8d 0%,#4a4a4a 45%,#1e1e1e 100%)}
.back-footer{top:692px;left:0;width:540px;height:68px;background:var(--white);border-bottom:6px solid var(--charcoal)}
.back-contact{font-size:12.5px;color:var(--ink);font-weight:500}
.back-web{font-size:8.5px;color:var(--ink);font-weight:500}
</style>
</head>
<body>

<section class="sheet sheet--front">
  <header class="abs front-header">
    <div class="brand"><span class="brand__dot"></span><span class="brand__name">Lumora Assist</span></div>
  </header>
  <div class="abs hero-photo" role="img" aria-label="Silhouetted business team meeting around a conference table in front of sunset windows"></div>
  <div class="abs hero-accent"></div>
  <h1 class="abs headline">Lumora Assist helps contact centers serve new customer access channels, improve customer service, &amp; lower costs of operation.</h1>

  <div class="abs intro">
    <div class="intro__body">
      <p>The huge popularity of social media and messaging is creating customer preferences to communicate with your company using SMS text messaging, ChatFlow, Teamline, Vocio, Voxa, HomeHub, and many other new channels.</p>
      <p>App fatigue has set in. Customers are weary of installing, updating and learning how to use mobile apps. Your customers want to communicate with you using their messaging service of choice or just talk into their smart phone, computer, Voxa or similar device.</p>
      <p>Sensible automation of customer interactions on these new channels can provide better service at even lower costs of operation.</p>
      <p>According to Marlow Research's report, by 2020, 85% of customer interactions will be managed without a human.</p>
      <p>Using specific techniques, Lumora Assist will help you shift some traffic from higher cost telephone calls to lower cost messaging channels. Shaping your traffic into lower cost channels has great financial benefits.</p>
    </div>
  </div>

  <div class="abs channels">
    <h2 class="channels__title"><span>Existing channels</span> have different costs</h2>
    <div class="channel-row">
      <svg class="channel-row__icon" viewBox="0 0 24 24"><path fill="#29a3dc" d="M6.6 10.8a15 15 0 0 0 6.6 6.6l2.2-2.2c.3-.3.7-.4 1-.2 1.1.4 2.3.6 3.6.6.6 0 1 .4 1 1V20c0 .6-.4 1-1 1A17 17 0 0 1 3 4c0-.6.4-1 1-1h3.5c.6 0 1 .4 1 1 0 1.3.2 2.5.6 3.6.1.3 0 .7-.2 1z"/></svg>
      <div class="channel-row__text">Telephone call with a live agent<br>Average cost per call is <em>$17*</em></div>
    </div>
    <div class="channel-row">
      <svg class="channel-row__icon" viewBox="0 0 24 24"><circle cx="12" cy="12" r="11" fill="#29a3dc"/><rect x="6.5" y="8" width="11" height="8" rx="1" fill="none" stroke="#fff" stroke-width="1.4"/><path d="M6.5 8.5l5.5 4 5.5-4" fill="none" stroke="#fff" stroke-width="1.4"/></svg>
      <div class="channel-row__text">Email with a live agent<br>Average cost per email is <em>$15*</em></div>
    </div>
    <div class="channel-row">
      <svg class="channel-row__icon" viewBox="0 0 24 24"><path fill="#29a3dc" d="M12 2c6 0 11 3.9 11 8.7s-5 8.7-11 8.7c-1 0-2-.1-2.9-.3L4 22l1.3-4.4A8.3 8.3 0 0 1 1 10.7C1 5.9 6 2 12 2z"/><text x="12" y="13.5" font-size="5.5" fill="#fff" text-anchor="middle" font-family="Roboto,Arial,sans-serif">LIVE</text></svg>
      <div class="channel-row__text">Webchat with a live agent<br>Average cost per web chat is <em>$12*</em></div>
    </div>
    <p class="footnote">*Above costs are sited from a CSR Institute research paper</p>
    <div class="cloud-photo" role="img" aria-label="Businessman touching a cloud computing interface with device icons"></div>
  </div>

  <footer class="abs front-footer">
    <div class="abs contact" style="top:12px;left:56px">
      <svg width="12" height="12" viewBox="0 0 24 24"><path fill="#29a3dc" d="M6.6 10.8a15 15 0 0 0 6.6 6.6l2.2-2.2c.3-.3.7-.4 1-.2 1.1.4 2.3.6 3.6.6.6 0 1 .4 1 1V20c0 .6-.4 1-1 1A17 17 0 0 1 3 4c0-.6.4-1 1-1h3.5c.6 0 1 .4 1 1 0 1.3.2 2.5.6 3.6.1.3 0 .7-.2 1z"/></svg>
      <span>555-014-2297</span>
    </div>
    <div class="abs front-footer__slash"></div>
    <div class="abs contact" style="top:12px;left:346px;font-size:8.8px">
      <svg width="12" height="12" viewBox="0 0 24 24"><circle cx="12" cy="12" r="10" fill="#29a3dc"/></svg>
      <span>www.lumoraassist.example</span>
    </div>
  </footer>
</section>

<section class="sheet sheet--back">
  <div class="abs back-top">
    <div class="abs app-strip">
      <div class="app"><span class="app__mark"></span>Voxa</div>
      <div class="app"><span class="app__mark"></span>TalkNest</div>
      <div class="app"><span class="app__mark"></span>PingApp</div>
      <div class="app"><span class="app__mark"></span>Teamline</div>
      <div class="app"><span class="app__mark"></span>HomeHub</div>
      <div class="app"><span class="app__mark"></span>ChatFlow</div>
      <div class="app"><span class="app__mark"></span>Zikko</div>
      <div class="app"><span class="app__mark"></span>SMS</div>
    </div>
    <p class="abs strip-note">With these new channels, the cost is similar to webchat. Carefully automated interactions are at an even lower cost</p>
  </div>

  <div class="abs engagement">
    <h2 class="section-title"><u>Engagement Model</u></h2>
    <h3 class="sub-title">Proposal</h3>
    <p>Lumora Assist provides a written proposal. The proposal will describe our engagement methodologies and costs.</p>
    <h3 class="sub-title">Engagement</h3>
    <p>Lumora Assist will meet with all the relevant stake holders on site and gather information to identify:</p>
    <ul class="ticks">
      <li>Historical traffic patterns.</li>
      <li>Actual costs by channel</li>
      <li>Review marketing plans that may impact customer service</li>
      <li>Review product plans that may impact customer service.</li>
      <li>Explore competition landscape as it relates to customer service.</li>
      <li>Review the existing corporate data store, analytics and reporting</li>
      <li>Review the current plans, metrics and budgets for customer service support</li>
    </ul>
    <h2 class="section-title" style="margin-top:6px"><u>Transformation</u> Report</h2>
    <ul class="ticks">
      <li>Executive summary</li>
      <li>Cost analysis per contact by channel</li>
      <li>Traffic patterns by channel</li>
      <li>Probable impacts of product and marketing plans</li>
      <li>Recommendations for achieving competitive advantage through service</li>
      <li>Recommendations for new channel types</li>
      <li>Recommendations for traffic shaping</li>
      <li>Near &amp; long-term options for sensible automation</li>
      <li>Technology recommendations for implementing new channels</li>
      <li>Projected financial impact of recommendations</li>
    </ul>
  </div>
  <div class="abs portrait-panel" role="img" aria-label="Monochrome businessman in a suit with a glowing circuit brain in place of a head"></div>

  <footer class="abs back-footer">
    <div class="abs brand" style="top:16px;left:34px"><span class="brand__dot"></span><span class="brand__name" style="font-size:15px">Lumora Assist</span></div>
    <div class="abs contact back-contact" style="top:12px;left:364px">
      <svg width="12" height="12" viewBox="0 0 24 24"><path fill="#29a3dc" d="M6.6 10.8a15 15 0 0 0 6.6 6.6l2.2-2.2c.3-.3.7-.4 1-.2 1.1.4 2.3.6 3.6.6.6 0 1 .4 1 1V20c0 .6-.4 1-1 1A17 17 0 0 1 3 4c0-.6.4-1 1-1h3.5c.6 0 1 .4 1 1 0 1.3.2 2.5.6 3.6.1.3 0 .7-.2 1z"/></svg>
      <span>555-014-2297</span>
    </div>
    <div class="abs contact back-web" style="top:36px;left:364px">
      <svg width="11" height="11" viewBox="0 0 24 24"><circle cx="12" cy="12" r="10" fill="#29a3dc"/></svg>
      <span>www.lumoraassist.example</span>
    </div>
  </footer>
</section>

</body>
</html>
```